Website Landing Page for Brightfall Systems

Create a custom designed website landing page for our business. Looking for a professional upscale design that incorporates our logo and logo colors into the theme. I want a standard fixed frame website, not a constant scrolling format that seems to be the trend. To start with I'm looking for more of the graphic design part, maybe a concept or theme, I don't expect to see a finished project. Not interested in generic templates or layouts.

The name of our company is Brightfall Systems and I've attached our logo below. I'd like to have the web page have the same look and feel of our logo, as well as the colors. Our company, Brightfall Systems does system design, installation, and programming, of residential and commercial Audio/Video and Automation systems. We do home theaters, lighting and building automation, video conferencing systems, security camera installations, conference rooms, projectors, distributed audio systems, and similar Technology projects. This will be a professional services/informational website. We will not sell products on this website. This website will be used to advertise our company and communicate our services to prospective customers. Having a well designed, professional and clean website is one way we want to distinguish our company from the competition.

Here are some examples of what I consider a professional well designed website
http://www.qorlamstudio.com/Work/

Last year we had our tradlo store designed (with PixelMarket) and I'm really happy with the way it turned out. You can see it at www.HolvenGearDepot.com I consider this to be a great design and looking for the same level of quality with this new website. However, do not copy or use any part of this design in this new project. This tradlo store is completely separate from our other company Brightfall Systems. I only mention this tradlo store an an example of good work.

Reason: Still going through designs.

Reason: Still working on project and have not had time to review all designs and request revisions.

Reason: Sill going through designs and requesting revisions

Reason: still going through all the submissions we received.

Target Market(s)

People interested in Audio/Video, home theaters, home automation. We do sales, system design, and programming. We typically work on larger projects with both residential and commercial customers.

Industry/Entity Type

Business

Number of Pages Required

1 page

Requirements
Must have
• Great design elements. Please use a white background. I think white goes well with our logo colors.

```html
<!DOCTYPE html>
<html lang="en">
<head>
<meta charset="utf-8">
<title>Brightfall Systems</title>
<link rel="stylesheet" href="https://fonts.googleapis.com/css2?family=Source+Sans+3:wght@400;600;700&display=swap">
<style>
:root{
  --blue:#3f86c7;
  --blue-dark:#2f74b9;
  --green:#5db847;
  --white:#ffffff;
  --ink:#1c1c1c;
  --font:"Source Sans 3", sans-serif;
}
*{box-sizing:border-box;margin:0;padding:0}
html,body{width:1200px;height:3061px;overflow:hidden;background:var(--white);font-family:var(--font);color:var(--ink)}
.page{position:relative;width:1200px;height:3061px}

/* header */
.site-header{position:absolute;left:0;top:0;width:1200px;height:118px;background:var(--white)}
.brand{position:absolute;left:131px;top:49px;font-size:22px;font-weight:600;color:var(--ink);line-height:1;white-space:nowrap}
.main-nav{position:absolute;top:54px;left:667px;display:flex}
.main-nav a{font-size:16.5px;font-weight:700;color:var(--blue-dark);text-decoration:none;text-transform:uppercase;margin-right:31px;white-space:nowrap}
.main-nav a:last-child{margin-right:0}

/* hero */
.hero{position:absolute;left:0;top:118px;width:1200px;height:482px;background:radial-gradient(ellipse at 50% 40%,#2b3a55 0%,#1a2438 55%,#0f1522 100%)}
.hero-frame{position:absolute;left:337px;top:155px;width:526px;height:172px;border:6px solid var(--green);display:flex;align-items:center;justify-content:center;text-align:center}
.hero-frame p{font-size:22px;font-weight:700;color:var(--green);text-transform:uppercase;line-height:28px}

/* section heading with rules */
.rule-title{display:flex;align-items:center;justify-content:center;gap:6px;font-weight:700;font-size:23px;text-transform:uppercase;line-height:1.2}
.rule-title::before,.rule-title::after{content:"";width:38px;height:2px;background:currentColor}
.rule-title.case-normal{text-transform:none}

/* about */
.about{position:absolute;left:0;top:600px;width:1200px;height:282px;background:var(--blue);color:var(--white);text-align:center;padding-top:70px}
.about p{width:790px;margin:18px auto 0;font-size:17.5px;line-height:22px}

/* services */
.services-title{position:absolute;left:0;top:936px;width:1200px;color:var(--ink)}
.service-photo{position:absolute;width:600px;height:421px}
.service-card{position:absolute;width:469px;height:421px;color:var(--white);display:flex;flex-direction:column;justify-content:center;align-items:center;text-align:center;padding:0 10px 20px}
.service-card p{margin-top:14px;font-size:17px;line-height:22px}
.card-green{background:var(--green)}
.card-blue{background:var(--blue)}
.photo-blueprint{left:0;top:1020px;background:linear-gradient(135deg,#e9e7e2 0%,#cfccc5 45%,#f1efea 100%)}
.card-design{left:600px;top:1020px}
.card-install{left:131px;top:1441px}
.photo-theater{left:600px;top:1441px;background:linear-gradient(180deg,#e5dccd 0%,#b59c7e 55%,#8a7462 100%)}
.photo-auditorium{left:0;top:1861px;background:linear-gradient(160deg,#c9ccd0 0%,#7e858e 50%,#3e4754 100%)}
.card-program{left:600px;top:1861px}

/* faq */
.faq{position:absolute;left:0;top:2282px;width:1200px;height:408px;background:linear-gradient(180deg,#4a5564 0%,#5d6672 45%,#3a4a43 100%)}
.faq-photo{position:absolute;left:180px;top:75px;width:245px;height:272px;background:linear-gradient(180deg,#2c5fa8 0%,#7d6a48 70%,#c59a55 100%)}
.faq-body{position:absolute;left:531px;top:134px;width:540px;color:var(--white)}
.faq-body .rule-title{justify-content:flex-start;margin-left:227px}
.faq-body p{margin-top:14px;font-size:17px;line-height:22px}

/* footer */
.site-footer{position:absolute;left:0;top:2690px;width:1200px;height:320px;background:var(--blue);color:var(--white)}
.footer-col{position:absolute;top:66px}
.footer-col h3{font-size:23px;font-weight:700;text-transform:uppercase;margin-bottom:20px}
.footer-col li{list-style:none;font-size:17px;line-height:21.6px}
.col-about{left:131px}.col-sector{left:410px}.col-wedo{left:610px}.col-sitemap{left:969px}
.copyright{position:absolute;left:0;top:3010px;width:1200px;height:51px;background:var(--green);color:var(--white);font-size:17px;display:flex;align-items:center;justify-content:center}
</style>
</head>
<body>
<div class="page">

  <header class="site-header">
    <div class="brand">Brightfall Systems</div>
    <nav class="main-nav">
      <a href="#about">About Us</a>
      <a href="#services">Services</a>
      <a href="#faq">FAQ</a>
      <a href="#contact">Contact Us</a>
    </nav>
  </header>

  <section class="hero" role="img" aria-label="Night view of an upscale building framed by palm trees">
    <div class="hero-frame">
      <p>We provide services for<br>audio/video and automation system<br>in private and commercial sectors</p>
    </div>
  </section>

  <section class="about" id="about">
    <h2 class="rule-title">About Us</h2>
    <p>Brightfall Systems does system design, installation, and programming, of residential and commercial Audio/Video and Automation systems. We do home theaters, lighting and building automation, video conferencing systems, security camera installations, conference rooms, projectors, distributed audio systems, etc.</p>
  </section>

  <h2 class="rule-title services-title" id="services">Services</h2>

  <div class="service-photo photo-blueprint" role="img" aria-label="Rolled blueprints lying on a technical drawing"></div>
  <div class="service-card card-green card-design">
    <h3 class="rule-title case-normal">System Design</h3>
    <p>Lorem Ipsum is simply dummy text of the printing and typesetting industry. Lorem Ipsum has been the industry's standard dummy text ever since the 1500s, when an unknown printer took a galley of type and scrambled it to make a type specimen book.</p>
  </div>

  <div class="service-card card-blue card-install">
    <h3 class="rule-title case-normal">Installation</h3>
    <p>Lorem Ipsum is simply dummy text of the printing and typesetting industry. Lorem Ipsum has been the industry's standard dummy text ever since the 1500s, when an unknown printer took a galley of type and scrambled it to make a type specimen book.</p>
  </div>
  <div class="service-photo photo-theater" role="img" aria-label="Living room home theater with a large screen and sectional sofa"></div>

  <div class="service-photo photo-auditorium" role="img" aria-label="Auditorium with rows of seats facing a projection screen"></div>
  <div class="service-card card-green card-program">
    <h3 class="rule-title case-normal">Programming</h3>
    <p>Lorem Ipsum is simply dummy text of the printing and typesetting industry. Lorem Ipsum has been the industry's standard dummy text ever since the 1500s, when an unknown printer took a galley of type and scrambled it to make a type specimen book.</p>
  </div>

  <section class="faq" id="faq" role="img" aria-label="City skyline under a cloudy sky">
    <div class="faq-photo" role="img" aria-label="Illuminated villa entrance with palm trees at dusk"></div>
    <div class="faq-body">
      <h2 class="rule-title">FAQ</h2>
      <p>Lorem Ipsum is simply dummy text of the printing and typesetting industry. Lorem Ipsum has been the industry's standard dummy text ever since the 1500s, when an unknown printer took a galley of type and scrambled it to make a type specimen book.</p>
    </div>
  </section>

  <footer class="site-footer" id="contact">
    <div class="footer-col col-about">
      <h3>About</h3>
      <ul><li>History</li><li>Leadership</li><li>Career</li></ul>
    </div>
    <div class="footer-col col-sector">
      <h3>Sector</h3>
      <ul><li>Private</li><li>Commercial</li></ul>
    </div>
    <div class="footer-col col-wedo">
      <h3>We Do</h3>
      <ul><li>Home Theaters</li><li>Lighting and Building Automation</li><li>Video Conference Systems</li><li>Security Camera Installations</li><li>Conference Room</li><li>Projecters</li><li>Distributed Audio Systems</li></ul>
    </div>
    <div class="footer-col col-sitemap">
      <h3>Site Map</h3>
      <ul><li>Terms Of Use</li><li>Privacy Policy</li></ul>
    </div>
  </footer>
  <div class="copyright">Copyright &copy; 2017 Brightfall Systems. All rights reserved.</div>

</div>
</body>
</html>
```